Infographic to communicate Cyber Security and Insurance Product Offering for IT Service Providers

We need an inspirational infographic that shows how TrellaWorks works with QDR (an MSP partner) to help organisations close the loop on cyber risk. The design should illustrate the layers of the IT infrastructure stack and the systems and processes that wrap around it to protect and mitigate against risk.
At the core: MSP Services (Desktop, Software, Website). Surrounding this: TrellaWorks Governance & Protection, leading into an Incident layer that connects to TrellaWorks Insurance and Incident Response, linked by a continuous feedback loop. The outer circle should represent the constant threat of cyber attack.
TrellaWorks core offerings for this graphic:
Plinth Verify (compliance/assurance product)
Plinth Cover
QDR Primary Services (directly connected to TrellaWorks):
Managed IT Services
Disaster Recovery as a Service (DRaaS)
E8 Security Packages
Cloud Hosting & Infrastructure
QDR Secondary Services (supporting but not directly anchored):
Telephony & Unified Communications
Networking Services
Data Backup & Storage Solutions
Professional Services & Consulting
Procurement & Licensing
Training & User Awareness
Style: Modern, professional, and client-friendly, with a technology-inspired colour palette.
Deliverables: Polished colour version plus editable source files — preferably in Figma, or alternatively if not possible using either Adobe Illustrator (.AI) or a layered Photoshop (.PSD) (e.g. industry standards for editable design).
Rewards: The winning design prize will be increased by $100, and we will also award $50 each to the 2nd and 3rd place runner-ups, as our way of giving a little more back.
A simple wireframe visual guide has been uploaded as a reference, but this should in no way limit or restrict your creativity. We encourage original, innovative approaches to bring this concept to life.
Ownership & Exclusivity: As per ArtMarquee’s T&Cs, all rights to the winning design will transfer to us once the project is complete for our ongoing use. We also kindly ask that the work created here remain exclusive to this project, meaning it won’t be reused or lightly modified for other clients in the future. The reason is simple: once we’ve invested in and paid for a design, we want to be confident it won’t turn up on a competitor’s website with just a different colour scheme. Thanks again for respecting that. [Note:- The designs submitted so far haven’t quite hit the mark, so I’ve put together a couple of slides to clarify direction. These outline the key stakeholders, the current IT services and challenges, how the Morvane product addresses those challenges, and a simple version of what we’d like the infographic to convey. Please review these slides carefully, as they should give you a clearer understanding of the story we want the design to tell.]
Target Market(s)
Small to Medium sized businesses
Colors
Designer to choose colors to be used in the design.
Look and feel

```html
<!DOCTYPE html>
<html lang="en">
<head>
<meta charset="utf-8">
<title>TrellaWorks – Closing the Loop on Cyber Risk</title>
<link rel="stylesheet" href="https://fonts.googleapis.com/css2?family=Montserrat:wght@600;700;800;900&display=swap">
<style>
  :root {
    --paper: #ffffff;
    --threat-red: #ed1c24;
    --threat-red-deep: #bf1e2d;
    --ring-blue: #c6ddf2;
    --loop-blue: #72b0e0;
    --brand-blue: #2a6db8;
    --panel-blue: #dceaf8;
    --navy: #08134a;
    --ink: #231f20;
    --white: #ffffff;
  }
  html, body {
    margin: 0;
    padding: 0;
    width: 1043px;
    height: 1200px;
    overflow: hidden;
    background: var(--paper);
  }
  .infographic {
    display: block;
    width: 1043px;
    height: 1200px;
    font-family: "Montserrat", sans-serif;
  }
  .threat-ring { fill: var(--threat-red); }
  .threat-ring-edge { fill: none; stroke: var(--threat-red-deep); stroke-width: 10; }
  .shield-ring { fill: var(--paper); stroke: var(--ring-blue); stroke-width: 20; }
  .threat-label {
    fill: var(--white);
    font-size: 28px;
    font-weight: 700;
    letter-spacing: 5px;
  }
  .feedback-label {
    fill: var(--brand-blue);
    font-size: 22px;
    font-weight: 700;
    letter-spacing: 3px;
  }
  .feedback-loop {
    fill: none;
    stroke: var(--loop-blue);
    stroke-width: 6;
  }
  .arrow-head { fill: var(--loop-blue); }
  .governance-panel { fill: var(--panel-blue); }
  .governance-text {
    fill: var(--brand-blue);
    font-size: 35px;
    font-weight: 800;
  }
  .partner-name {
    fill: var(--brand-blue);
    font-size: 86px;
    font-weight: 800;
  }
  .partner-sub {
    fill: var(--ink);
    font-size: 42px;
    font-weight: 800;
  }
  .stack-base { fill: url(#stackGlow); }
  .stack-layer {
    fill: var(--navy);
    stroke: var(--brand-blue);
    stroke-width: 3;
  }
  .stack-text {
    fill: var(--white);
    font-size: 44px;
    font-weight: 800;
  }
  .incident-box { fill: var(--brand-blue); }
  .band-shadow { fill: #cfcfcf; }
  .band-text {
    fill: var(--white);
    font-size: 33px;
    font-weight: 800;
  }
  .headline {
    fill: var(--navy);
    font-size: 150px;
    font-weight: 900;
  }
  .tagline {
    fill: var(--brand-blue);
    font-size: 66px;
    font-weight: 800;
  }
</style>
</head>
<body>
<svg class="infographic" viewBox="0 0 1043 1200" xmlns="http://www.w3.org/2000/svg" role="img" aria-label="TrellaWorks: closing the loop on cyber risk">
  <defs>
    <linearGradient id="stackGlow" x1="0" y1="0" x2="1" y2="0">
      <stop offset="0" stop-color="#1f55a6"/>
      <stop offset="0.5" stop-color="#5fa8ec"/>
      <stop offset="1" stop-color="#1f55a6"/>
    </linearGradient>
    <radialGradient id="ringSheen" cx="0.5" cy="0.5" r="0.5">
      <stop offset="0.82" stop-color="#ffffff" stop-opacity="0"/>
      <stop offset="0.9" stop-color="#ffb3a0" stop-opacity="0.45"/>
      <stop offset="1" stop-color="#ffffff" stop-opacity="0"/>
    </radialGradient>
    <marker id="loopArrow" viewBox="0 0 20 20" refX="6" refY="10" markerWidth="9" markerHeight="9" orient="auto-start-reverse" markerUnits="strokeWidth">
      <path class="arrow-head" d="M0 0 L20 10 L0 20 L5 10 Z"/>
    </marker>
    <path id="threatPathClockwise" d="M 925 1371 A 503 503 0 1 1 925 365 A 503 503 0 1 1 925 1371"/>
    <path id="threatPathBottom" d="M 388 868 A 537 537 0 0 0 1462 868"/>
  </defs>

  <g transform="translate(44 0) scale(0.7) translate(-243 -173)">
    <!-- Outer threat ring -->
    <circle class="threat-ring" cx="925" cy="868" r="575"/>
    <path d="M 400 680 A 560 560 0 0 1 710 350" fill="none" stroke="#ff9a86" stroke-opacity="0.55" stroke-width="16" stroke-linecap="round"/>
    <path d="M 1140 350 A 560 560 0 0 1 1450 680" fill="none" stroke="#ff9a86" stroke-opacity="0.55" stroke-width="16" stroke-linecap="round"/>
    <circle class="threat-ring-edge" cx="925" cy="868" r="486"/>
    <circle class="shield-ring" cx="925" cy="868" r="470"/>

    <text class="threat-label" text-anchor="middle"><textPath href="#threatPathClockwise" startOffset="25%">CYBER ATTACK</textPath></text>
    <text class="threat-label" text-anchor="middle"><textPath href="#threatPathClockwise" startOffset="50%">CYBER ATTACK</textPath></text>
    <text class="threat-label" text-anchor="middle"><textPath href="#threatPathClockwise" startOffset="75%">CYBER ATTACK</textPath></text>
    <text class="threat-label" text-anchor="middle" dy="-4"><textPath href="#threatPathBottom" startOffset="50%">CYBER ATTACK</textPath></text>

    <!-- Feedback loop -->
    <path class="feedback-loop" d="M 728 540 A 395 395 0 0 0 652 1150" marker-start="url(#loopArrow)" marker-end="url(#loopArrow)"/>
    <path class="feedback-loop" d="M 1122 540 A 395 395 0 0 1 1198 1150" marker-start="url(#loopArrow)" marker-end="url(#loopArrow)"/>

    <text class="feedback-label" text-anchor="middle" transform="translate(512 862) rotate(-90)">FEEDBACK</text>
    <text class="feedback-label" text-anchor="middle" transform="translate(595 862) rotate(-90)">FEEDBACK</text>
    <text class="feedback-label" text-anchor="middle" transform="translate(1262 862) rotate(90)">FEEDBACK</text>
    <text class="feedback-label" text-anchor="middle" transform="translate(1341 862) rotate(90)">FEEDBACK</text>

    <!-- Governance & protection -->
    <rect class="governance-panel" x="769" y="456" width="311" height="118" rx="10"/>
    <text class="governance-text" x="925" y="508" text-anchor="middle" textLength="270" lengthAdjust="spacingAndGlyphs">TRELLAWORKS</text>
    <text class="governance-text" x="925" y="547" text-anchor="middle">GOVERNANCE</text>
    <rect class="governance-panel" x="769" y="586" width="311" height="62" rx="8"/>
    <text class="governance-text" x="925" y="630" text-anchor="middle">PROTECTION,</text>

    <!-- MSP services core -->
    <text class="partner-name" x="925" y="757" text-anchor="middle">QDR MSP</text>
    <text class="partner-sub" x="925" y="801" text-anchor="middle">SERVICES</text>

    <rect class="stack-base" x="705" y="832" width="438" height="228" rx="16"/>
    <rect class="stack-layer" x="684" y="843" width="481" height="62" rx="6"/>
    <text class="stack-text" x="925" y="890" text-anchor="middle">DESKTOP</text>
    <rect class="stack-layer" x="684" y="915" width="481" height="62" rx="6"/>
    <text class="stack-text" x="925" y="962" text-anchor="middle">SOFTWARE</text>
    <rect class="stack-layer" x="684" y="987" width="481" height="62" rx="6"/>
    <text class="stack-text" x="925" y="1034" text-anchor="middle">WEBSITE</text>

    <!-- Incident layer -->
    <rect class="incident-box" x="708" y="1130" width="433" height="62" rx="5"/>
    <text class="band-text" x="925" y="1173" text-anchor="middle">INCIDENT</text>

    <rect class="band-shadow" x="441" y="1224" width="967" height="62" rx="6"/>
    <rect class="incident-box" x="441" y="1213" width="967" height="62" rx="4"/>
    <text class="band-text" x="925" y="1256" text-anchor="middle" textLength="900" lengthAdjust="spacingAndGlyphs">INCIDENT RESPONSE  •  TRELLAWORKS INSURANCE</text>

    <!-- Headline -->
    <text class="headline" x="910" y="1615" text-anchor="middle" textLength="940" lengthAdjust="spacingAndGlyphs">TRELLAWORKS</text>
    <text class="tagline" x="910" y="1700" text-anchor="middle">CLOSING THE LOOP ON</text>
    <text class="tagline" x="910" y="1767" text-anchor="middle">CYBER RISK</text>
  </g>
</svg>
</body>
</html>
```